Quovix Pinbrook Page, Post and ADV Format

Quovix.net is a startup that has developed a plugin for e-commerce which understands pinbrook users engagement and gives them an economic value users can spend as discount on e-commerce partners. We are now changing our brand identity and you can see more about our goals in the attachment. WE NEED this Pinbrook contents:
– quotes (layout of images with texts)
– real time marketing
– gif of products you offer
– about us images
– carousel ads/posts
-- cover

. Complete Brief and brand identity is detailed in the attachment.

Target Market(s)

B2B and B2C. Pinbrook users and e-commerce managers.

Industry/Entity Type

It Company

Requirements
Must have
• Pinbrook contents:
• – quotes (layout of images with texts)
• – real time marketing
• – gif of products you offer
• – about us images
• – carousel ads/posts
• -- cover

```html
<!DOCTYPE html>
<html lang="en">
<head>
<meta charset="UTF-8">
<title>Quovix — Quote Post</title>
<link href="https://fonts.googleapis.com/css2?family=Lato:ital,wght@0,300;1,700&display=swap" rel="stylesheet">
<style>
  :root {
    --page-bg: #1c1c1c;
    --card-black: #050505;
    --sky-light: #f4f4f4;
    --sky-mid: #8a8a8a;
    --sky-dark: #2b2b2b;
    --quote-text: #e6e6e6;
    --author-text: #d9d4d4;
  }
  html, body {
    margin: 0;
    padding: 0;
    width: 1200px;
    height: 1200px;
    overflow: hidden;
    background: var(--page-bg);
  }
  .quote-post {
    position: absolute;
    left: 0;
    top: 286px;
    width: 1200px;
    height: 628px;
    background: var(--card-black);
    overflow: hidden;
  }
  .quote-post__photo {
    position: absolute;
    inset: 0;
    background:
      radial-gradient(ellipse 300px 200px at 60px 470px, var(--sky-light) 0%, rgba(244,244,244,0.6) 45%, rgba(244,244,244,0) 100%),
      linear-gradient(100deg, var(--sky-mid) 0%, var(--sky-dark) 38%, var(--card-black) 52%, var(--card-black) 100%);
  }
  .quote-post__text {
    position: absolute;
    left: 872px;
    top: 228px;
    transform: translateX(-50%);
    width: 560px;
    text-align: center;
    font-family: "Lato", sans-serif;
  }
  .quote-post__quote {
    margin: 0;
    font-weight: 300;
    font-size: 41px;
    line-height: 55px;
    letter-spacing: 0.5px;
    text-transform: uppercase;
    color: var(--quote-text);
  }
  .quote-post__mark {
    font-weight: 700;
    font-size: 34px;
    vertical-align: 10px;
  }
  .quote-post__author {
    margin: 14px 0 0;
    padding-right: 10px;
    text-align: right;
    font-weight: 700;
    font-style: italic;
    font-size: 21px;
    letter-spacing: -0.3px;
    text-transform: uppercase;
    color: var(--author-text);
  }
</style>
</head>
<body>
  <section class="quote-post">
    <div class="quote-post__photo" role="img" aria-label="Black and white photo of a climber silhouetted on a steep rock face against a bright, sunlit sky"></div>
    <div class="quote-post__text">
      <p class="quote-post__quote"><span class="quote-post__mark">&ldquo;</span>Strength and growth<br>come only<br>through continuous<br>effort and struggle.<span class="quote-post__mark">&rdquo;</span></p>
      <p class="quote-post__author">- Harlan Voss</p>
    </div>
  </section>
</body>
</html>
```